Im looking for a sleek and sexy business card, that resembles elite or VIP status status.
our business is marnivoss.com
you can view our products on there, but our main audience for handing out our cards will be for people in the hospitality industry, so it will need to impress high management and CEO of hotels and restaurants, bars, clubs etc...
the card features will have UV spot on both sides, 400gsm stock. standard size.
Artwork should be 86 x 54mm + 2mm bleed = 90 x 58mm
it should have a nice "unique" uv spot pattern that highlights the card, not a repeated pattern, theres no originality there, and it will be disregarded.
The written material will be:
Marni Voss Hospitality College (logo)
Dena Whitby
Director
Phone: 1300 561 437
Mobile: 0439 817 265
Email: info@marnivoss.com
website: www.marnivoss.com
I'm looking for originality here, i don't want just a simple stock card, want something that has a wow factor for people.
You will find the logo attached. you may invert the white to black words to suit the background as you please.
thank you and good luck
As a side note, ive received a lot of proposals, im too busy to give feedback to each and every one, so if i havent provided feedback for your design within 24 hours, then consider it not acceptable, and you could resubmit another design.
So far i have not seen any design that stood out for me, they all seem pretty generic. there nothing thats unique, i would figure for the amount that im offering, that people would put some more effort and creativity into the design.
so far over 200 designs submitted, and nothing i have seen looks very original, everything looks like a different variation of the same stuff, i said it very clearly i wanted something unique, the only thing that has come close to it so far is this one
Reason: Ive received alot of design concepts and i have reviewed everyone, but i havent had time to give feedback to every single one, only the ones that have interested me, if i havent responded, its because i havent found it good enough.
so far only a few design have been on par with what ive been looking for, an attractive eye popping design.
heres a few of them,
http://files.pitchgallery.net/design_img/51846/62937/62937_2846105_51846_image.jpg
http://files.pitchgallery.net/design_img/51846/58714/58714_2846592_51846_image.jpg
theyre, both unique and original, and eye catching, the only thing theyre missing is the sexyness.
if you still think you have some creativity left in your minds, then throw it on here.
Reason: Sorry guys for the delay, I was in a serious accident and out of commission for the past few months, I'm just slowly recovering now, please bare with me as i try to attend to this project, it may take me awhile as I have other projects that are on standby, I'm not 100% at the moment, so im extending the deadline for 2 weeks right now. Thanks for your patience.

```html
<!DOCTYPE html>
<html lang="en">
<head>
<meta charset="utf-8">
<title>Marni Voss Hospitality College – Business Card</title>
<link rel="stylesheet" href="https://fonts.googleapis.com/css2?family=Open+Sans:wght@400;600;700&display=swap">
<style>
  :root {
    --backdrop: #e8e6e3;
    --card-dark: #1c1c1d;
    --card-mid: #2b2b2d;
    --accent-blue: #4fa7e0;
    --text-white: #ffffff;
    --divider: #8a8a8a;
  }
  html, body {
    margin: 0;
    padding: 0;
    width: 992px;
    height: 1200px;
    overflow: hidden;
    background: var(--backdrop);
    font-family: "Open Sans", Arial, sans-serif;
  }
  .canvas {
    position: relative;
    width: 992px;
    height: 1200px;
  }
  .card {
    position: absolute;
    width: 672px;
    height: 424px;
    border-radius: 212px 0 0 212px;
    overflow: hidden;
    box-shadow: 0 6px 18px rgba(0,0,0,0.25);
  }
  .card-front { left: 122px; top: 154px; }
  .card-back  { left: 106px; top: 645px; }
  .card-surface {
    position: absolute;
    inset: 0;
    background: radial-gradient(ellipse at 45% 45%, var(--card-mid) 0%, var(--card-dark) 75%);
  }
  .brand-lockup {
    position: absolute;
    left: 50px;
    top: 150px;
    display: flex;
    align-items: center;
    gap: 12px;
  }
  .brand-dot {
    width: 22px;
    height: 22px;
    border-radius: 50%;
    background: var(--accent-blue);
    flex: none;
  }
  .brand-name {
    width: 250px;
    color: var(--text-white);
    font-weight: 600;
    font-size: 25px;
    line-height: 1.15;
    text-transform: uppercase;
    letter-spacing: 0.5px;
  }
  .divider {
    position: absolute;
    left: 369px;
    top: 122px;
    width: 2px;
    height: 200px;
    background: linear-gradient(to bottom, transparent, var(--divider) 25%, var(--divider) 75%, transparent);
  }
  .contact-block {
    position: absolute;
    left: 386px;
    top: 110px;
    color: var(--text-white);
  }
  .person-name {
    margin: 0;
    color: var(--accent-blue);
    font-weight: 700;
    font-size: 26px;
    line-height: 34px;
  }
  .person-title {
    margin: 0 0 22px;
    font-size: 20px;
    line-height: 26px;
  }
  .contact-list {
    list-style: none;
    margin: 0;
    padding: 0;
  }
  .contact-list li {
    display: flex;
    align-items: center;
    gap: 8px;
    font-size: 18px;
    line-height: 30px;
  }
  .contact-icon {
    width: 15px;
    height: 15px;
    flex: none;
  }
  .back-name {
    position: absolute;
    left: 0;
    right: 0;
    top: 150px;
    text-align: center;
    padding-left: 60px;
    color: var(--text-white);
    font-weight: 700;
    font-size: 58px;
    line-height: 1.05;
    text-transform: uppercase;
  }
</style>
</head>
<body>
<div class="canvas">

  <section class="card card-front">
    <div class="card-surface" role="img" aria-label="Dark card surface with subtle spot-gloss hexagon texture"></div>

    <div class="brand-lockup">
      <span class="brand-dot"></span>
      <span class="brand-name">Marni Voss Hospitality College</span>
    </div>

    <div class="divider"></div>

    <div class="contact-block">
      <h1 class="person-name">Dena Whitby</h1>
      <p class="person-title">Director</p>
      <ul class="contact-list">
        <li>
          <svg class="contact-icon" viewBox="0 0 16 16" aria-hidden="true"><path fill="#fff" d="M3.5 1.5l2.5 3-1.5 1.7c.8 1.8 2.2 3.2 4 4l1.7-1.5 3 2.5-1.4 2.3C6.5 13.3 2.7 9.5 1.2 3z"/></svg>
          1300 561 437
        </li>
        <li>
          <svg class="contact-icon" viewBox="0 0 16 16" aria-hidden="true"><rect x="4" y="1" width="8" height="14" rx="1.5" fill="#fff"/><rect x="5.5" y="3" width="5" height="6" fill="#1c1c1d"/><circle cx="8" cy="12.3" r="1" fill="#1c1c1d"/></svg>
          0439 817 265
        </li>
        <li>
          <svg class="contact-icon" viewBox="0 0 16 16" aria-hidden="true"><rect x="1" y="4" width="14" height="9" rx="1" fill="#fff"/><path d="M1.5 4.5L8 9l6.5-4.5" stroke="#1c1c1d" stroke-width="1.3" fill="none"/></svg>
          info@marnivoss.com
        </li>
        <li>
          <svg class="contact-icon" viewBox="0 0 16 16" aria-hidden="true"><g fill="none" stroke="#fff" stroke-width="1.3"><circle cx="8" cy="8" r="6.5"/><ellipse cx="8" cy="8" rx="3" ry="6.5"/><path d="M1.5 8h13"/></g></svg>
          www.marnivoss.com
        </li>
      </ul>
    </div>
  </section>

  <section class="card card-back">
    <div class="card-surface" role="img" aria-label="Dark card surface with subtle spot-gloss hexagon texture"></div>
    <p class="back-name">Marni Voss<br>Hospitality College</p>
  </section>

</div>
</body>
</html>
```